Re-design of our website - Property Development Company

Our current website is now old and stale. We are looking for a Wordpress design for a new website. Our company is a property development and property investment company. We have different projects that are under construction and have completed a number also. We would like to showcase these projects as individual pages. The projects are located all over the east coast of Australia and a mixture of retail, industrial, residential subdivsions. In the near future we are hoping to start a small property funds management division as well.

Current website is www.korvanith.com.au

We are wanting you to design a page for the each of following (total of 3 pages):
- Home page
- Project page (which will be used to showcase each development project). There are 4 active projects that we currently own and a number of completed projects.
- Information page (which will be used for about us, contact us, management etc.)

Feel free to go out of the box and wow us. We are open to new ideas.
Updates

Reason: Hi I am going on annual leave for a week being 17-21 Feb so wont be able to comment on anyones design so I have given you an extra week and a bit to finish off your 3 pages. Thanks for the designs so far, they are looking good.

Target Market(s)

It will be used by business professionals researching our company including:
- current investors
- new investors
- consultants (architects, builders, town planners, council, real estate managers/agents, engineers etc.)
- Bank lenders

We want these people to think yes we want to work with this company, they look like they are exceptional at what they do, professional, highly capable.

Industry/Entity Type

Investment

Requirements
Must have
• Our Logo. Files attached. This can be modified if you think it needs to be improved.
Nice to have
• We like clean looking websites.
• We will have some professional photographs taken of our current property developments once they are completed - two shopping centres that will be our signature developments to date. For the time being I have uploaded some aerial photographs on one of our projects under construction and also some nice photos of one of our completed developments. This should help with designing the project page.
Should not have
• We don't like busy websites with too much going on and you don't know what to look at.

```html
<!DOCTYPE html>
<html lang="en">
<head>
<meta charset="utf-8">
<title>Korvanith Partners – Home</title>
<link href="https://fonts.googleapis.com/css2?family=Lato:wght@300;400&display=swap" rel="stylesheet">
<style>
:root{
  --blue:#0b6fc6;
  --blue-dark:#0a5fae;
  --blue-soft:#7ea6dc;
  --page:#f1f1f3;
  --panel:#ffffff;
  --text:#444448;
  --nav:#3a3a3e;
  --rule:#c9c9cc;
  --hero-a:#0d73cc;
  --hero-b:#0a62b5;
}
*{box-sizing:border-box;margin:0;padding:0}
html,body{width:1200px;height:1162px;overflow:hidden}
body{background:var(--page);font-family:"Lato",Arial,sans-serif;color:var(--text);position:relative}
.stripe{position:absolute;left:0;width:1200px;height:3px;
  background:repeating-linear-gradient(90deg,var(--blue) 0 46px,var(--blue-soft) 46px 92px)}
.stripe.top{top:0}.stripe.bottom{bottom:0;height:4px}
.site-header{position:absolute;top:3px;left:0;width:1200px;height:109px}
.brand{position:absolute;left:188px;top:38px;display:flex;align-items:center;gap:8px;
  font-size:20px;font-weight:400;color:var(--blue)}
.brand-mark{width:14px;height:14px;background:var(--blue)}
.main-nav{position:absolute;top:47px;left:436px;display:flex;gap:29px;font-size:12px;color:var(--nav)}
.main-nav .active{color:var(--blue)}
.login{position:absolute;left:888px;top:0;width:130px;height:109px;
  border-left:1px solid var(--rule);border-right:1px solid var(--rule)}
.login svg{position:absolute;left:24px;top:38px}
.login-label{position:absolute;left:66px;top:44px;font-size:11.5px;line-height:14px;color:var(--nav)}
.hero{position:absolute;top:112px;left:0;width:1200px;height:328px;
  background:linear-gradient(160deg,var(--hero-a),var(--hero-b))}
.hero-copy{position:absolute;left:269px;top:116px;color:#fff}
.hero-title{font-size:51px;font-weight:400;line-height:56px}
.hero-sub{font-size:22px;font-weight:400;line-height:24px;margin-left:1px}
.panel{position:absolute;background:var(--panel);box-shadow:0 1px 2px rgba(0,0,0,.18)}
.card{top:462px;width:250px;height:250px}
.card-photo{height:130px;background:linear-gradient(160deg,#c8352f,#6f7b60 60%,#3d4a5a)}
.card p{padding:14px 14px 0;font-size:9.6px;font-weight:300;line-height:12px}
.rule{position:absolute;left:189px;width:822px;height:1px;background:var(--rule)}
.panel-title{font-size:18px;font-weight:400;color:var(--blue);margin-bottom:10px}
.panel-body{padding:12px 14px}
.panel-body p{font-size:9.6px;font-weight:300;line-height:12px;margin-bottom:12px}
.panel-body ul{list-style:none;margin:0 0 12px 8px}
.panel-body li{font-size:9.6px;font-weight:300;line-height:12px}
.panel-body li::before{content:"• "}
.site-footer{position:absolute;top:1111px;left:0;width:1200px;text-align:center;font-size:9.6px;font-weight:300;line-height:17px}
.site-footer u{text-decoration:underline}
</style>
</head>
<body>
<div class="stripe top"></div>

<header class="site-header">
  <div class="brand"><span class="brand-mark"></span>Korvanith Partners</div>
  <nav class="main-nav">
    <span class="active">Home</span><span>Philosophy</span><span>Activities &amp; Projects</span><span>Management</span><span>File Upload</span>
  </nav>
  <div class="login">
    <svg width="34" height="34" viewBox="0 0 34 34" aria-hidden="true">
      <path d="M11 8a6 7 0 0 1 12 0v5a6 7 0 0 1-12 0z" fill="#3c3c40"/>
      <path d="M2 34c0-8 6-12 15-12s15 4 15 12z" fill="#3c3c40"/>
    </svg>
    <div class="login-label">Partner<br>Login</div>
  </div>
</header>

<section class="hero" role="img" aria-label="Aerial view of a commercial development site tinted blue">
  <div class="hero-copy">
    <div class="hero-title">Success</div>
    <div class="hero-sub">Through Discipline</div>
  </div>
</section>

<article class="panel card" style="left:189px">
  <div class="card-photo" role="img" aria-label="Crowd at the opening of a red-fronted retail store"></div>
  <p>Lorem Ipsum is simply dummy text of the printing and typesetting industry. Lorem Ipsum has been the industry's standard dummy text ever since the 1500s, when an unknown printer took a galley of type and scrambled it to make a type specimen book. It has survived not only five centuries, but also the leap into electronic typesetting, remaining essentially unchanged.</p>
</article>
<article class="panel card" style="left:475px">
  <div class="card-photo" role="img" aria-label="Red retail shopfront with banners and trees"></div>
  <p>Lorem Ipsum is simply dummy text of the printing and typesetting industry. Lorem Ipsum has been the industry's standard dummy text ever since the 1500s, when an unknown printer took a galley of type and scrambled it to make a type specimen book. It has survived not only five centuries, but also the leap into electronic typesetting, remaining essentially unchanged.</p>
</article>
<article class="panel card" style="left:761px">
  <div class="card-photo" role="img" aria-label="Completed bulky goods retail centre with car park"></div>
  <p>Lorem Ipsum is simply dummy text of the printing and typesetting industry. Lorem Ipsum has been the industry's standard dummy text ever since the 1500s, when an unknown printer took a galley of type and scrambled it to make a type specimen book. It has survived not only five centuries, but also the leap into electronic typesetting, remaining essentially unchanged.</p>
</article>

<div class="rule" style="top:727px"></div>

<section class="panel" style="left:189px;top:742px;width:535px;height:158px">
  <div class="panel-body">
    <h2 class="panel-title">Korvanith Partners</h2>
    <p>Having started operations in 2001, Korvanith Partners is an established “value add” property group with a focus on property development.</p>
    <p>Korvanith Partners is an opportunistic total return investor / developer with the proven capability to successfully identify, acquire, manage and deliver property projects that are anticipated to deliver strong returns to our group and partners.</p>
    <p>Through the projects we have created and participated in over the years, Korvanith Partners has refined substantial skill sets in the areas of bulky goods, retail, industrial and commercial development.</p>
  </div>
</section>
<section class="panel" style="left:761px;top:742px;width:250px;height:158px">
  <div class="panel-body"><h2 class="panel-title">Korvanith Capital</h2></div>
</section>

<section class="panel" style="left:189px;top:915px;width:822px;height:172px">
  <div class="panel-body">
    <p>Our next wave of projects have been acquired during 2010 and 2011 and include a number of retail and residential developments in growth locations across the eastern seaboard from as far north as Mackay in Queensland down to Launceston in Tasmania.</p>
    <p>Looking ahead, 2012 will see us focused on advancing the delivery of these five projects whilst looking to acquire new projects in the second half of the year.</p>
    <p>With strong capital resources and an appetite for more projects, 2012 is likely to see us continue our attraction to:</p>
    <ul>
      <li>Retail development sites</li>
      <li>Infill retail development for both bulky goods and pure retail</li>
      <li>Value add opportunities in industrial, commercial and retail</li>
    </ul>
    <p>For further details on our existing projects see the Projects section.</p>
  </div>
</section>

<div class="rule" style="top:1100px"></div>

<footer class="site-footer">
  Copyright 2014 Korvanith Partners. All Rights Reserved. <u>Terms of Use</u> | Website Designed by Brightline Studio<br>
  Disclaimer | Contact
</footer>

<div class="stripe bottom"></div>
</body>
</html>
```